Lantern Software Overview Brochure

Lantern Software has developed a cloud based accounting systems for small businesses that have out grown products like Brightfern. We need an overview brochure that can be delivered in a PDF and become incorporated into our web site. I have attached our logo as a reference for colors and style.

The brochure should be speak to small business owners and communicate why Lantern is better for them than Brightfern. I will be happy to provide screen shots and content.

Target Market(s)

companies between 10 and 200 employees

Industry/Entity Type

Small Business

Requirements
Must have
• Strong branding around the Lantern name and logo. Room for screen shots of the software and discussion of product features.

```html
<!DOCTYPE html>
<html lang="en">
<head>
<meta charset="utf-8">
<title>Lantern Software Overview Flyer</title>
<link rel="stylesheet" href="https://fonts.googleapis.com/css2?family=Open+Sans:wght@400;600;700;800&display=swap">
<style>
  :root {
    --brand-red: #c00d0d;
    --paper: #ffffff;
    --backdrop: #e4e4e4;
    --word-revenue: #d4b55c;
    --word-sales: #3fc192;
    --word-purchasing: #4d89cc;
    --word-financials: #ea7a2c;
    --word-brand: #82b34c;
    --word-settings: #f2f2f2;
    --word-marketing: #d88c8c;
    --word-service: #d23030;
  }
  * { box-sizing: border-box; margin: 0; padding: 0; }
  html, body { width: 1200px; height: 831px; overflow: hidden; }
  body {
    background: var(--backdrop);
    font-family: "Open Sans", Arial, sans-serif;
    display: flex; align-items: center; justify-content: center;
  }
  .flyer {
    width: 540px; height: 790px;
    background: var(--paper);
    box-shadow: 0 6px 18px rgba(0,0,0,.25);
    display: flex; flex-direction: column;
  }
  .flyer-header {
    height: 88px; background: var(--brand-red);
    display: flex; align-items: center; justify-content: space-between;
    padding: 0 26px; color: var(--paper);
  }
  .brand { display: flex; align-items: center; gap: 10px; }
  .brand-dot { width: 34px; height: 34px; border-radius: 50%; background: var(--paper); }
  .brand-name { font-weight: 600; font-size: 20px; letter-spacing: 1px; text-transform: uppercase; white-space: nowrap; }
  .tagline { font-weight: 700; font-size: 12.5px; letter-spacing: .6px; text-transform: uppercase; white-space: nowrap; }
  .feature-grid { display: block; margin: 10px 0 0; }
  .word-cloud text { font-family: "Open Sans", Arial, sans-serif; }
  .flyer-footer {
    margin-top: 12px; flex: 1;
    background: var(--brand-red); color: var(--paper);
    padding: 26px 26px 0;
  }
  .headline { font-size: 20px; font-weight: 800; text-transform: uppercase; letter-spacing: .3px; white-space: nowrap; }
  .headline span { font-weight: 400; font-size: 15px; letter-spacing: .2px; }
  .contacts { display: flex; gap: 16px; margin-top: 18px; font-size: 12px; font-weight: 600; white-space: nowrap; }
  .contact { display: flex; align-items: center; gap: 6px; }
  .contact svg { width: 16px; height: 16px; flex: none; fill: none; stroke: var(--paper); stroke-width: 1.6; }
</style>
</head>
<body>
  <article class="flyer">
    <header class="flyer-header">
      <div class="brand">
        <span class="brand-dot"></span>
        <span class="brand-name">Lantern Software</span>
      </div>
      <p class="tagline">Providing the best services</p>
    </header>

    <svg class="feature-grid" width="540" height="530" viewBox="0 0 540 530">
      <defs>
        <linearGradient id="tech-photo-tone" x1="0" y1="0" x2="1" y2="1">
          <stop offset="0" stop-color="#9a9db3"/>
          <stop offset=".55" stop-color="#5a5d75"/>
          <stop offset="1" stop-color="#2e3044"/>
        </linearGradient>
        <radialGradient id="tech-photo-glow" cx=".35" cy=".45" r=".55">
          <stop offset="0" stop-color="#c9d3ea" stop-opacity=".55"/>
          <stop offset="1" stop-color="#c9d3ea" stop-opacity="0"/>
        </radialGradient>
        <linearGradient id="woman-photo-tone" x1="0" y1="0" x2="1" y2="1">
          <stop offset="0" stop-color="#4f536a"/>
          <stop offset=".6" stop-color="#8c8199"/>
          <stop offset="1" stop-color="#b9a9b8"/>
        </linearGradient>
        <radialGradient id="woman-photo-glow" cx=".3" cy=".3" r=".5">
          <stop offset="0" stop-color="#b8cce6" stop-opacity=".5"/>
          <stop offset="1" stop-color="#b8cce6" stop-opacity="0"/>
        </radialGradient>
        <radialGradient id="cloud-tone" cx=".55" cy=".5" r=".6">
          <stop offset="0" stop-color="#4d4d4d"/>
          <stop offset="1" stop-color="#2a2a2a"/>
        </radialGradient>
      </defs>

      <g class="photo-panel" role="img" aria-label="Photo of a businessman touching a futuristic digital interface">
        <path d="M0 0 H405 L380 116 L256 180 H0 Z" fill="url(#tech-photo-tone)"/>
        <path d="M0 0 H405 L380 116 L256 180 H0 Z" fill="url(#tech-photo-glow)"/>
      </g>
      <path class="accent-panel" d="M422 0 H540 V226 L524 230 L398 124 Z" fill="var(--brand-red)"/>
      <g class="photo-panel" role="img" aria-label="Photo of a woman holding a tablet and tapping a holographic chart">
        <path d="M0 194 H248 L226 336 L338 440 L314 530 H0 Z" fill="url(#woman-photo-tone)"/>
        <path d="M0 194 H248 L226 336 L338 440 L314 530 H0 Z" fill="url(#woman-photo-glow)"/>
      </g>
      <path class="cloud-panel" d="M262 196 L392 128 L520 236 L510 366 L356 428 L240 334 Z" fill="url(#cloud-tone)"/>
      <path class="accent-panel" d="M532 250 H540 V530 H328 L354 444 L522 378 Z" fill="var(--brand-red)"/>

      <g class="word-cloud">
        <text x="372" y="218" font-size="18" font-weight="600" fill="var(--word-revenue)">Revenue</text>
        <text x="300" y="248" font-size="19" fill="var(--word-sales)">Sales</text>
        <text x="360" y="260" font-size="19" fill="var(--word-purchasing)">Purchasing</text>
        <text x="268" y="300" font-size="40" fill="var(--word-financials)">Financials</text>
        <text x="250" y="328" font-size="17" fill="var(--word-brand)">Lantern</text>
        <text x="352" y="338" font-size="24" fill="var(--word-settings)">Settings</text>
        <text x="284" y="372" font-size="32" fill="var(--word-marketing)">Marketing</text>
        <text x="332" y="406" font-size="19" font-weight="600" fill="var(--word-service)">Service</text>
      </g>
    </svg>

    <footer class="flyer-footer">
      <h1 class="headline">Innovative services <span>for grow your business</span></h1>
      <div class="contacts">
        <span class="contact">
          <svg viewBox="0 0 16 16"><rect x="4" y="1.5" width="8" height="13" rx="1.5"/><line x1="7" y1="12" x2="9" y2="12"/></svg>
          555 013 2847
        </span>
        <span class="contact">
          <svg viewBox="0 0 16 16"><rect x="1.5" y="3.5" width="13" height="9" rx="1"/><polyline points="1.5,4 8,9 14.5,4"/></svg>
          info@lanternsoftware.com
        </span>
        <span class="contact">
          <svg viewBox="0 0 16 16"><circle cx="8" cy="8" r="6.5"/><ellipse cx="8" cy="8" rx="3" ry="6.5"/><line x1="1.5" y1="8" x2="14.5" y2="8"/></svg>
          www.lanternsoftware.com
        </span>
      </div>
    </footer>
  </article>
</body>
</html>
```